Criação de Kit Layout de Posts para Redes Sociais (Facebook, Instagram e etc) para Roupas, Jóias & acessórios
" Funcionará por internet site e Instagram "

```html
<!DOCTYPE html>
<html lang="pt-BR">
<head>
<meta charset="UTF-8">
<title>Moda Praia – Post</title>
<link href="https://fonts.googleapis.com/css2?family=Bodoni+Moda:opsz,wght@6..96,400;6..96,500&display=swap" rel="stylesheet">
<style>
  :root {
    --ink: #111111;
    --paper: #f4f3f3;
    --stripe-zone: #ececec;
    --panel: rgba(214, 166, 180, 0.72);
    --photo-top: #d3e2e7;
    --photo-bottom: #e9dccb;
  }
  html, body {
    margin: 0;
    padding: 0;
    width: 1200px;
    height: 1200px;
    overflow: hidden;
    background: var(--paper);
  }
  .post {
    position: relative;
    width: 1200px;
    height: 1200px;
    overflow: hidden;
    font-family: "Bodoni Moda", "Didot", serif;
    color: var(--ink);
  }
  .beach-photo {
    position: absolute;
    left: 0;
    top: 0;
    width: 768px;
    height: 1200px;
    background: linear-gradient(180deg, var(--photo-top) 0%, var(--photo-bottom) 100%);
  }
  .texture-side {
    position: absolute;
    left: 768px;
    top: 0;
    width: 432px;
    height: 1200px;
    background: linear-gradient(180deg, var(--paper), var(--stripe-zone));
  }
  .color-panel {
    position: absolute;
    left: 595px;
    top: 79px;
    width: 514px;
    height: 1030px;
    background: var(--panel);
  }
  .headline {
    position: absolute;
    right: 115px;
    top: 92px;
    margin: 0;
    text-align: right;
    font-weight: 400;
    font-size: 124px;
    line-height: 118px;
    letter-spacing: 1px;
  }
  .collection {
    position: absolute;
    left: 688px;
    top: 1030px;
    margin: 0;
    font-weight: 400;
    font-size: 52px;
    line-height: 1;
    letter-spacing: 1px;
  }
  .tagline {
    position: absolute;
    left: 1132px;
    top: 652px;
    writing-mode: vertical-rl;
    font-size: 20px;
    letter-spacing: 2px;
    white-space: nowrap;
  }
  .contact {
    position: absolute;
    left: 806px;
    top: 1128px;
    display: flex;
    align-items: center;
    gap: 12px;
    font-size: 21px;
    letter-spacing: 0.5px;
  }
  .contact-dot {
    width: 28px;
    height: 28px;
    border: 2.5px solid var(--ink);
    border-radius: 50%;
    box-sizing: border-box;
  }
</style>
</head>
<body>
  <main class="post">
    <div class="beach-photo" role="img" aria-label="Fotografia de moda praia: mulher caminhando na areia com chapéu de palha, saia longa florida e bolsa de palha"></div>
    <div class="texture-side"></div>
    <div class="color-panel"></div>

    <h1 class="headline">SEU<br>TEXTO<br>AQUI</h1>
    <p class="collection">MODA PRAIA</p>
    <div class="tagline">CONFECÇÃO DE BOLSAS E UTILITÁRIOS</div>

    <div class="contact">
      <span class="contact-dot"></span>
      <span class="contact-text">REDESOCIAL/CONTATO</span>
    </div>
  </main>
</body>
</html>
```